Website design in Wordpress for Golf Simulator Center

We are opening a new golf simulator center in Copenhagen, and need a website design. We are using wordpress, and our site is https://vornlo-tee.dk
We will need a design for the frontpage, and a design for subpages (which we will be reusing for all subpages).
Logo is as seen on the site, and our base color scheme is leaf green.
As text, take the text on the current website, or put some placeholder text in english.
Should be responsive and look good on both desktop and mobile.
Target Market(s)
Male, 18-60, golf players

```html
<!DOCTYPE html>
<html lang="en">
<head>
<meta charset="utf-8">
<title>Vornlo Tee – Golf Simulator in Valby</title>
<link rel="stylesheet" href="https://fonts.googleapis.com/css2?family=Oswald:wght@400;500;600&family=Roboto+Condensed:wght@400;700&display=swap">
<style>
:root{
  --green:#087d08;
  --green-dark:#066206;
  --ink:#222;
  --text:#555;
  --grey-bg:#f3f3f3;
  --white:#fff;
  --black:#111;
}
*{box-sizing:border-box;margin:0;padding:0}
html,body{width:1200px;height:3495px;overflow:hidden}
body{position:relative;background:var(--white);font-family:"Roboto Condensed",Arial,sans-serif;color:var(--ink)}
.abs{position:absolute}
.heading{font-family:"Oswald",Arial,sans-serif;font-weight:500;text-transform:uppercase;color:var(--ink);line-height:1.15}
.rule{position:absolute;height:3px;width:92px;background:var(--green)}
.btn-outline{position:absolute;display:flex;align-items:center;justify-content:center;border:3px solid var(--green);border-radius:30px;font-family:"Roboto Condensed",sans-serif;font-weight:700;font-size:13px;text-transform:uppercase;color:var(--ink);text-decoration:none}

/* header */
.site-header{position:absolute;left:0;top:0;width:1200px;height:87px;background:var(--white)}
.brand{position:absolute;left:110px;top:24px;display:flex;align-items:center;gap:8px;font-family:"Oswald",sans-serif;font-weight:600;font-size:28px;color:var(--green);text-transform:uppercase}
.brand-mark{width:18px;height:18px;background:var(--green)}
.nav{position:absolute;top:36px;left:451px;display:flex;gap:30px;font-size:13px;font-weight:700;text-transform:uppercase}
.nav a{color:var(--ink);text-decoration:none}
.nav a.active{color:var(--green);position:relative}
.nav a.active::before{content:"";position:absolute;left:0;right:0;top:-36px;height:3px;background:var(--green)}
.quote{left:948px;top:22px;width:139px;height:42px}

/* hero */
.hero-photo{left:0;top:87px;width:600px;height:599px;background:linear-gradient(180deg,#3c74c9 0%,#7cb36a 45%,#3f7d2c 80%,#1d2a1a 100%)}
.hero-dark{left:600px;top:87px;width:600px;height:120px;background:#1a1f1a}
.hero-title{left:677px;top:298px;color:var(--white);font-size:56px;font-weight:400;line-height:1.05}
.hero-sub{left:677px;top:436px;color:var(--white);font-family:"Oswald",sans-serif;font-size:19px;text-transform:uppercase}
.hero-btn{left:678px;top:483px;width:140px;height:41px;border-color:var(--white);color:var(--white)}
.dots{left:678px;top:650px;display:flex;gap:8px}
.dots span{width:13px;height:13px;border-radius:50%;border:2px solid var(--white)}
.dots span.on{background:var(--white)}

/* intro */
.intro-title{left:110px;top:862px;font-size:40px;font-weight:500}
.intro-rule{left:112px;top:975px}
.intro-copy{left:110px;top:996px;width:466px;font-size:13px;line-height:25.6px;color:var(--text);text-align:justify}
.intro-copy p+p{margin-top:25px}
.learn{left:112px;top:1222px;width:140px;height:41px}
.frame{left:983px;top:845px;width:127px;height:121px;border:3px solid var(--black)}
.intro-photo{left:630px;top:871px;width:459px;height:392px;background:linear-gradient(160deg,#1e2421 0%,#2f3a33 40%,#5f8a3a 75%,#4c7a2d 100%)}

/* blog */
.blog{left:0;top:1365px;width:1200px;height:688px;background:var(--grey-bg)}
.center-title{width:1200px;left:0;text-align:center;font-size:40px}
.card{position:absolute;top:1557px;width:471px;height:394px;background:var(--white);box-shadow:0 2px 8px rgba(0,0,0,.08)}
.card-img{height:262px}
.card-date{position:absolute;left:20px;top:242px;background:var(--green);color:var(--white);font-size:13px;padding:3px 7px}
.card h3{position:absolute;left:20px;top:280px;font-weight:400;font-size:20px;color:var(--ink)}
.card p{position:absolute;left:20px;top:318px;width:430px;font-size:13px;line-height:25.6px;color:var(--text)}
.card-go{position:absolute;right:0;bottom:0;width:32px;height:30px;background:var(--green);display:flex;align-items:center;justify-content:center}
.arrow{position:absolute;top:1739px;width:33px;height:33px;border-radius:50%;background:#bdbdbd;display:flex;align-items:center;justify-content:center}

/* map */
.map{left:187px;top:2246px;width:826px;height:366px;background:linear-gradient(90deg,#e6e6e4 0%,#ececea 55%,#a9c6f0 75%,#8fb5ea 100%)}
.map-note{left:205px;top:2264px;width:211px;height:76px;background:var(--white);padding:14px 0 0 20px;font-size:13px;line-height:26px;color:var(--ink)}
.zoom{left:963px;top:2534px;width:40px;height:70px;background:var(--white);box-shadow:0 1px 4px rgba(0,0,0,.25);font-size:24px;text-align:center;line-height:34px;color:#666}

/* contact */
.contact-title{left:109px;top:2852px;font-size:54px;font-weight:400;color:var(--white)}
.contact-lead{left:112px;top:2934px;font-size:16px;color:var(--white)}
.field{position:absolute;background:var(--white);border-radius:4px;font-size:13px;color:#666;padding:18px 20px}
.send{left:112px;top:3240px;width:112px;height:50px;background:var(--black);color:var(--white);border-radius:4px;display:flex;align-items:center;justify-content:center;font-weight:700;font-size:13px;text-transform:uppercase}
.footer-note{left:0;width:1200px;top:3383px;text-align:center;font-size:13px;color:#333}
.social{left:522px;top:3420px;display:flex;gap:4px}
.social span{width:36px;height:36px;border-radius:50%;background:var(--black);display:flex;align-items:center;justify-content:center}
</style>
</head>
<body>

<header class="site-header">
  <div class="brand"><span>Vornlo Tee</span><span class="brand-mark"></span></div>
  <nav class="nav">
    <a class="active" href="#">Home</a>
    <a href="#">Blog</a>
    <a href="#">Find your way</a>
    <a href="#">Dictionary</a>
    <a href="#">Contact us</a>
  </nav>
  <a class="btn-outline quote" href="#">Get a quote</a>
</header>

<!-- hero -->
<div class="abs hero-photo" role="img" aria-label="Golfer swinging in front of a simulator screen showing a fairway"></div>
<div class="abs hero-dark" role="img" aria-label="Dark simulator bay interior"></div>
<svg class="abs" style="left:600px;top:87px" width="600" height="676" viewBox="0 0 600 676">
  <polygon points="0,0 600,72 600,603 0,675" fill="#087d08"/>
</svg>
<h1 class="abs heading hero-title">Golf simulator<br>in Valby</h1>
<p class="abs hero-sub">Indoor golf center with 8 simulators in Valby.</p>
<a class="btn-outline hero-btn" href="#">Get started</a>
<div class="abs dots"><span class="on"></span><span></span><span></span><span></span></div>

<!-- intro -->
<h2 class="abs heading intro-title">Golf simulator in Valby<br>opens January 2023</h2>
<div class="rule intro-rule"></div>
<div class="abs intro-copy">
  <p>In January 2023, a new golf simulator center will open in Valby with 8 simulators of the Radarline 4 type. We look forward to being able to welcome new and experienced golfers. With us, you can practice all kinds of shots indoors, sheltered from rain and snow, or play an entire 18-hole course in half the time.</p>
  <p>Each simulator gives you a precise radar measurement of your stroke, so you can practice exactly as you want on a virtual driving range, or on one of our many virtual courses from around the world.</p>
</div>
<a class="btn-outline learn" href="#">Learn more&nbsp;
  <svg width="12" height="12" viewBox="0 0 12 12"><circle cx="6" cy="6" r="6" fill="#111"/><path d="M5 3.5 7.5 6 5 8.5" stroke="#fff" stroke-width="1.6" fill="none"/></svg></a>
<div class="abs frame"></div>
<svg class="abs" style="left:598px;top:1145px" width="150" height="150">
  <defs><pattern id="dotgrid" width="15.5" height="15.5" patternUnits="userSpaceOnUse"><circle cx="2" cy="2" r="1.5" fill="#333"/></pattern></defs>
  <rect x="0" y="0" width="20" height="150" fill="url(#dotgrid)"/>
  <rect x="0" y="120" width="150" height="30" fill="url(#dotgrid)"/>
</svg>
<div class="abs intro-photo" role="img" aria-label="Empty simulator bay with a golf bag on green turf"></div>

<!-- blog -->
<section class="abs blog"></section>
<h2 class="abs heading center-title" style="top:1458px">Latest blog</h2>
<div class="rule" style="left:554px;top:1526px"></div>
<div class="arrow" style="left:39px"><svg width="8" height="10"><path d="M6 1 2 5l4 4" stroke="#555" fill="none" stroke-width="1.3"/></svg></div>
<div class="arrow" style="left:1128px"><svg width="8" height="10"><path d="M2 1l4 4-4 4" stroke="#555" fill="none" stroke-width="1.3"/></svg></div>

<article class="card" style="left:111px">
  <div class="card-img" role="img" aria-label="Golfer hitting a shot in a simulator bay" style="background:linear-gradient(160deg,#1d2620,#3f5e45 45%,#5b8a3c 100%)"></div>
  <span class="card-date">Dec 22, 2022</span>
  <h3>The first blow has been struck!</h3>
  <p>The first blow on the first simulator has been struck, and now we just need to have the other 7 completed.</p>
  <a class="card-go" href="#"><svg width="10" height="10"><path d="M1 2l3 3-3 3M5 2l3 3-3 3" stroke="#fff" fill="none" stroke-width="1.5"/></svg></a>
</article>
<article class="card" style="left:618px">
  <div class="card-img" role="img" aria-label="Two golfers training on a simulator with a city sunset target range" style="background:linear-gradient(180deg,#3b4f7a,#c9874a 40%,#3a5a30 80%,#1c2a1c)"></div>
  <span class="card-date">Aug 04, 2022</span>
  <h3>Golf training on a simulator</h3>
  <p>Golf training can be done directly on a golf simulator at Vornlo Tee in Valby. Here you get the opportunity to train with a Pro, or train yourself.</p>
  <a class="card-go" href="#"><svg width="10" height="10"><path d="M1 2l3 3-3 3M5 2l3 3-3 3" stroke="#fff" fill="none" stroke-width="1.5"/></svg></a>
</article>

<!-- map -->
<h2 class="abs heading center-title" style="top:2148px">Find your way to Vornlo Tee</h2>
<div class="rule" style="left:554px;top:2214px"></div>
<div class="abs map" role="img" aria-label="Street map of Copenhagen showing the center location"></div>
<div class="abs map-note">123,Lorem ipsum dolor sit am<br>consectetur</div>
<div class="abs zoom">+<br>−</div>

<!-- contact -->
<svg class="abs" style="left:0;top:2714px" width="1200" height="713" viewBox="0 0 1200 713">
  <polygon points="0,0 600,77 600,598 0,675" fill="#087d08"/>
  <polygon points="600,77 1200,0 1200,712 600,598" fill="#4a8fd0"/>
</svg>
<div class="abs" role="img" aria-label="Colourful harbour houses and sailing boats in Copenhagen" style="left:600px;top:2791px;width:600px;height:520px;background:linear-gradient(180deg,#6fa7dc 0%,#c9573a 45%,#e0b23c 65%,#2f5f8d 100%);clip-path:polygon(0 0,100% -15%,100% 118%,0 100%)"></div>
<h2 class="abs heading contact-title">Contact us</h2>
<p class="abs contact-lead">Write to us via the form below, or directly at info@vornlo-tee.dk</p>
<div class="field" style="left:112px;top:2953px;width:206px;height:51px">Name</div>
<div class="field" style="left:330px;top:2953px;width:206px;height:51px">Email address</div>
<div class="field" style="left:112px;top:3017px;width:424px;height:51px">Subject</div>
<div class="field" style="left:112px;top:3083px;width:424px;height:135px">Your message</div>
<div class="abs send">Send now</div>

<p class="abs footer-note">© Copyrights 2023 The Company Name | All Rights Reserved</p>
<div class="abs social">
  <span aria-label="Social profile 1"></span>
  <span aria-label="Social profile 2"></span>
  <span aria-label="Video channel"></span>
  <span aria-label="Email"><svg width="14" height="10"><rect x="0.5" y="0.5" width="13" height="9" fill="#fff"/><path d="M0.5 0.5 7 5.5l6.5-5" stroke="#111" fill="none"/></svg></span>
</div>

</body>
</html>
```